Front and back cover design for skincare marketing materials

Thank you for showing an interest in my project.
Project Details.

I require a front and back cover for our marketing materials.
·       Front Cover size: 105 mm W x 150 mm H.
·       Back Cover size:  105 mm W x 150 mm H.
·       It must include these two colors. You can use a third color if you wish.
1.     #DBA09D
2.     #FFFFFF
 
Front Cover
·      The front cover will have a faded image of the Kakadu Plum branch and fruit. There are two image files, KP_image-1.jpg and kp_image-2.jpeg. You can use both images, just a portion of them, or source alternative royalty-free images of Kakadu Plum that may better fit the design. These two files have been uploaded.
 
The front cover wording.
Top of the front cover.
a.     The title of the image. “Kakadu Plum”
b.     The brand name, “Velora Skincare”. The file brand_name.ai uploaded.
 
Bottom of the front cover- Designer's choice of font.
The bottom of the front cover contains three lines of text in the following order.  
1.     Australian Native Ingredients
2.     100% Natural · Organic · Wild-harvested
3.     Australian-Made Premium Skincare
 
Back Cover
·      Back Cover wording.The back cover contains the following words "grown by nature" in white (#FFFFFF) of font Italianno (font_file.ttf) with a background color of #DBA09D as seen in the sample box (sample_box.pdf) right-side panel
 
Please provide one file for the front cover and a separate file for the back cover.
All the elements of the files must be editable.
 
Do NOT use the Curve function on the files, as the text must remain editable/changeable.
 
All assets/resources/files, including fonts not supplied by us but used by the designer, must be named and provided with the finished design.
Updates

Slow to provide project details.

Target Market(s)

Beauty-minded Asian consumers between the ages of 32 and 75 who take a proactive approach to maintaining younger-looking skin. Those who already know the danger of skin damage caused by skincare containing harsh chemicals choose effective natural/organic solutions to meet their skincare needs. Those who wish a more radiant glow and youthful appearance to their skin. Usually, a two-income middle to high-income bracket couples with a mindset for health and beauty.

Industry/Entity Type

beauty

Font styles to use
Other font styles liked:
• I will provide a font file and a brand name file.

Requirements
Must have
• You must use the two colors provided on the product box. The designer may use a third color.
Nice to have
• some gold colour

```html
<!DOCTYPE html>
<html lang="en">
<head>
<meta charset="utf-8">
<title>Velora Skincare – Kakadu Plum Covers</title>
<link href="https://fonts.googleapis.com/css2?family=Italianno&family=Pinyon+Script&family=Montserrat:wght@500&family=Poppins:wght@500;600&display=swap" rel="stylesheet">
<style>
  :root {
    --rose: #dba09d;
    --rose-deep: #c98580;
    --white: #ffffff;
    --ink: #111111;
    --cream: #fbf3e4;
    --leaf: #a9b94a;
    --stage: #a8a8a8;
  }
  * { margin: 0; padding: 0; box-sizing: border-box; }
  html, body { width: 1200px; height: 1135px; overflow: hidden; }
  body { background: var(--stage); position: relative; font-family: "Poppins", sans-serif; }

  .cover { position: absolute; top: 216px; width: 492px; height: 702px; overflow: hidden; }
  .cover--front { left: 86px; }
  .cover--back { left: 622px; background: var(--rose); }

  .hero-photo {
    position: absolute; inset: 0;
    background:
      radial-gradient(ellipse 190px 230px at 410px 190px, rgba(169,185,74,.95), rgba(190,200,110,.6) 60%, rgba(240,220,180,0) 100%),
      radial-gradient(ellipse 260px 220px at 40px 40px, rgba(255,255,250,.95), rgba(255,250,235,0) 100%),
      linear-gradient(180deg, var(--cream) 0%, #f3dcc2 35%, #e9b7a8 60%, var(--rose) 100%);
  }

  .brand {
    position: absolute; left: 30px; top: 70px;
    font-family: "Poppins", sans-serif; font-weight: 600;
    font-size: 24px; letter-spacing: .12em; text-transform: uppercase;
    color: var(--rose-deep);
  }

  .product-title {
    position: absolute; left: 0; right: 0; top: 336px; text-align: center;
    font-family: "Pinyon Script", cursive; font-weight: 400; font-size: 124px; line-height: 1;
    color: var(--ink);
  }
  .product-subtitle {
    position: absolute; left: 0; right: 0; top: 446px; text-align: center;
    font-family: "Montserrat", sans-serif; font-weight: 500;
    font-size: 64px; line-height: 1; letter-spacing: .3em; padding-left: .3em;
    color: var(--white);
  }

  .features { position: absolute; left: 0; right: 0; top: 528px; height: 120px; }
  .feature { position: absolute; top: 0; width: 150px; margin-left: -75px; text-align: center; }
  .feature:nth-child(1) { left: 98px; }
  .feature:nth-child(2) { left: 243px; }
  .feature:nth-child(3) { left: 391px; }
  .feature-icon {
    display: block; width: 46px; height: 46px; margin: 0 auto 14px;
    border-radius: 50%; border: 2px solid var(--white);
  }
  .feature-text {
    font-size: 14px; font-weight: 500; line-height: 17px; color: var(--ink);
  }
  .divider { position: absolute; top: 4px; width: 1px; height: 112px; background: rgba(255,255,255,.7); }
  .divider--a { left: 174px; }
  .divider--b { left: 318px; }

  .tagline {
    position: absolute; left: 0; right: 0; top: 666px; text-align: center;
    font-size: 15px; font-weight: 600; letter-spacing: .2em; color: var(--white);
  }

  .back-slogan {
    position: absolute; left: 50%; top: 50%;
    width: max-content;
    transform: translate(-50%, -50%) rotate(-90deg);
    white-space: nowrap;
    font-family: "Italianno", cursive; font-size: 116px; line-height: 1;
    color: var(--white);
  }
</style>
</head>
<body>
  <section class="cover cover--front">
    <div class="hero-photo" role="img" aria-label="Faded photo of a Kakadu plum branch with green fruit against soft blossom"></div>
    <div class="brand">Velora Skincare</div>
    <h1 class="product-title">Kakadu</h1>
    <div class="product-subtitle">PLUM</div>
    <div class="features">
      <div class="feature"><span class="feature-icon"></span><p class="feature-text">Australian<br>Native<br>Ingredients</p></div>
      <div class="feature"><span class="feature-icon"></span><p class="feature-text">100% Natural<br>Organic<br>Wild-harvested</p></div>
      <div class="feature"><span class="feature-icon"></span><p class="feature-text">Australian-Made<br>Premium<br>Skincare</p></div>
      <span class="divider divider--a"></span>
      <span class="divider divider--b"></span>
    </div>
    <div class="tagline">AUSTRALIAN SUPERFOODS</div>
  </section>

  <section class="cover cover--back">
    <p class="back-slogan">grown by nature</p>
  </section>
</body>
</html>
```